We need visit card and a letter paper for our website. thx

We have a beauty clinic in Switzerland.
https://wiesentalblick.ch
We need a visit card.

Requirements
Must have
• see colors on website

```html
<!DOCTYPE html>
<html lang="de">
<head>
<meta charset="utf-8">
<title>Wiesentalblick – Visitenkarte</title>
<link rel="stylesheet" href="https://fonts.googleapis.com/css2?family=Lato:wght@300;400;900&display=swap">
<style>
  :root {
    --backdrop: #5c5c5c;
    --card-white: #ffffff;
    --brand-pink: #d04c7a;
    --ink: #111111;
    --ink-soft: #4a4a4a;
    --rule: #8a8a8a;
  }
  * { box-sizing: border-box; margin: 0; padding: 0; }
  html, body { width: 1200px; height: 900px; overflow: hidden; }
  body {
    background: var(--backdrop);
    font-family: "Lato", sans-serif;
    display: flex;
    flex-direction: column;
    align-items: center;
    justify-content: center;
    gap: 56px;
  }
  .card {
    width: 560px;
    height: 320px;
    border-radius: 18px;
    position: relative;
    overflow: hidden;
  }
  /* Back side */
  .card--back {
    background: var(--brand-pink);
    color: var(--card-white);
    display: flex;
    flex-direction: column;
    align-items: center;
    justify-content: center;
    gap: 36px;
  }
  .card--back .brand-name {
    font-size: 50px;
    font-weight: 300;
    letter-spacing: 0.5px;
  }
  .card--back .web {
    font-size: 15px;
    font-weight: 300;
    letter-spacing: 3px;
  }
  /* Front side */
  .card--front {
    background: var(--card-white);
    color: var(--ink);
    display: flex;
    align-items: center;
    padding: 0 40px;
  }
  .front-brand {
    width: 230px;
    font-size: 30px;
    font-weight: 300;
    color: var(--ink);
  }
  .divider {
    width: 1px;
    height: 170px;
    background: var(--rule);
    margin: 0 34px 0 10px;
  }
  .contact { display: flex; flex-direction: column; }
  .contact .person {
    font-size: 25px;
    font-weight: 900;
    line-height: 1.1;
  }
  .contact .role,
  .contact .address {
    font-size: 14px;
    color: var(--ink-soft);
    line-height: 1.35;
  }
  .contact .role { margin-bottom: 8px; }
  .contact .address { margin-bottom: 10px; }
  .contact-list { list-style: none; }
  .contact-list li {
    display: flex;
    align-items: center;
    gap: 8px;
    font-size: 14px;
    color: var(--ink-soft);
    line-height: 1.5;
  }
  .contact-list svg { width: 13px; height: 13px; flex: none; }
</style>
</head>
<body>

  <section class="card card--back">
    <div class="brand-name">Wiesentalblick</div>
    <div class="web">www.wiesentalblick.ch</div>
  </section>

  <section class="card card--front">
    <div class="front-brand">Wiesentalblick</div>
    <div class="divider"></div>
    <div class="contact">
      <div class="person">Dr. Lea Brunner</div>
      <div class="role">Founder &amp; CEO</div>
      <div class="address">Talstrasse 22, 4418<br>Reigoldswil, Switzerland</div>
      <ul class="contact-list">
        <li>
          <svg viewBox="0 0 16 16" aria-hidden="true"><path d="M4 1.5l2.5 3-1.5 1.8c.8 1.8 2.2 3.2 4 4l1.8-1.5 3 2.5-1.6 2.2C7.5 13.3 2.7 8.5 2 3.1z" fill="#111"/></svg>
          +41 (0) 800 24 36 58
        </li>
        <li>
          <svg viewBox="0 0 16 16" aria-hidden="true"><rect x="1" y="3" width="14" height="10" fill="#111"/><path d="M1 3l7 6 7-6" stroke="#fff" stroke-width="1.3" fill="none"/></svg>
          hallo@wiesentalblick.ch
        </li>
        <li>
          <svg viewBox="0 0 16 16" aria-hidden="true"><circle cx="8" cy="8" r="6.5" fill="none" stroke="#111" stroke-width="1.3"/><path d="M1.5 8h13M8 1.5c-3 3.5-3 9.5 0 13M8 1.5c3 3.5 3 9.5 0 13" fill="none" stroke="#111" stroke-width="1"/></svg>
          www.wiesentalblick.ch
        </li>
      </ul>
    </div>
  </section>

</body>
</html>
```